Business Card for staff member of football club FC Brenor

I would like to get a business card template for all staff member of our soccer club.

The card should use as much as possible the 2 colors of the club : Red which is the main color and blue which is the alternative color. It can be balanced between the two like our logo.

I prefer simple and lean design.

Contact Information for Business Card

Bussiness card should have all main stuff as describe here below in must have.

Font styles to use
Sans Serif

Requirements
Must have
• Name : Mathieu DERLAPIN
Fonction : Président
Mobile : +41 xx xxx xx xx
Email : first.lastname@fcbrenor.example
Adresse of the club : FC Brenor, 4821 Brenor
Website of the club : www.fcbrenor.example
Nice to have
• Version with and without picture of the staff member

A version for men, a version for women staff member.

```html
<!DOCTYPE html>
<html lang="fr">
<head>
<meta charset="utf-8">
<title>FC Brenor – Carte de visite</title>
<link rel="stylesheet" href="https://fonts.googleapis.com/css2?family=Roboto:wght@300;400;500;700&display=swap">
<style>
  :root {
    --page: #e6e6e5;
    --card: #403f45;
    --card-back: #3b3a40;
    --red: #e3213a;
    --white: #f1f1f2;
    --grey: #c9c9cc;
    --rule: #8d8c92;
  }
  * { box-sizing: border-box; margin: 0; padding: 0; }
  html, body {
    width: 1200px; height: 801px; overflow: hidden;
    background: var(--page);
    font-family: "Roboto", Arial, sans-serif;
  }
  .sheet {
    width: 1200px; height: 801px;
    display: flex; align-items: center; justify-content: center; gap: 40px;
  }
  .card {
    position: relative;
    width: 540px; height: 310px;
    border-bottom: 5px solid var(--red);
    box-shadow: 0 10px 24px rgba(0,0,0,.18);
  }
  .card--front { background: var(--card); }
  .card--back { background: var(--card-back); }

  .club-name {
    position: absolute; top: 62px; left: 0; right: 0;
    display: flex; align-items: center; justify-content: center; gap: 12px;
    color: var(--white); font-weight: 700; font-size: 30px; letter-spacing: .5px;
  }
  .club-name__dot { width: 18px; height: 18px; background: var(--red); }

  .person {
    position: absolute; right: 256px; top: 206px; text-align: right;
  }
  .person__name { color: var(--red); font-weight: 500; font-size: 19px; }
  .person__role { color: var(--grey); font-weight: 300; font-size: 14px; margin-top: 4px; }

  .divider {
    position: absolute; left: 292px; top: 180px;
    width: 1px; height: 98px; background: var(--rule);
  }

  .contact {
    position: absolute; left: 310px; top: 184px;
    list-style: none; color: var(--grey); font-weight: 300; font-size: 12.5px;
  }
  .contact li { display: flex; align-items: center; gap: 8px; height: 22px; white-space: nowrap; }
  .contact svg { width: 12px; height: 12px; flex: none; }
  .contact .no-icon { padding-left: 20px; }

  .back-name {
    position: absolute; right: 36px; bottom: 34px;
    color: var(--white); font-weight: 700; font-size: 56px; letter-spacing: 1px;
  }
</style>
</head>
<body>
<main class="sheet">
  <section class="card card--front" aria-label="Recto">
    <div class="club-name"><span class="club-name__dot"></span>FC Brenor</div>

    <div class="person">
      <p class="person__name">Mathieu DERLAPIN</p>
      <p class="person__role">Président</p>
    </div>

    <div class="divider"></div>

    <ul class="contact">
      <li>
        <svg viewBox="0 0 12 12" aria-hidden="true"><path d="M2.5 1 L4.5 1 L5 3.5 L3.8 4.4 Q4.8 6.6 7.6 8.2 L8.5 7 L11 7.5 L11 9.5 Q10.5 11 9 11 Q1 10 1 2.5 Q1 1 2.5 1 Z" fill="var(--red)"/></svg>
        +41 xx xxx xx xx
      </li>
      <li>
        <svg viewBox="0 0 12 12" aria-hidden="true"><rect x="1" y="2.5" width="10" height="7" fill="none" stroke="var(--red)" stroke-width="1.2"/><path d="M1 2.5 L6 6.5 L11 2.5" fill="none" stroke="var(--red)" stroke-width="1.2"/></svg>
        first.lastname@fcbrenor.example
      </li>
      <li>
        <svg viewBox="0 0 12 12" aria-hidden="true"><circle cx="6" cy="6" r="5" fill="none" stroke="var(--red)" stroke-width="1.2"/><ellipse cx="6" cy="6" rx="2.2" ry="5" fill="none" stroke="var(--red)" stroke-width="1"/><path d="M1 6 H11" stroke="var(--red)" stroke-width="1"/></svg>
        www.fcbrenor.example
      </li>
      <li class="no-icon">FC Brenor, 4821 Brenor</li>
    </ul>
  </section>

  <section class="card card--back" aria-label="Verso">
    <p class="back-name">FC Brenor</p>
  </section>
</main>
</body>
</html>
```